Team email banner for internal communications

We need a team email banner/header that will be applied to all internal communications from our department to other functions. The graphic should be optimized for Outlook and be landscape in layout. We have 5 different silo within our team and will need so will either need have a blank space to denote each team or have change in colors/graphics to denote each team (see current headers attached to job description). We are looking for a banner that combines our team logo (attached) with our team name, Regional Talent & Coaching Unit. The theme should be L&D and pharmaceutical in nature.

Need extra days to review

The text in the banner should be Regional Talent & Coaching Unit with the team logo (attached).

```html
<!DOCTYPE html>
<html lang="en">
<head>
<meta charset="utf-8">
<title>Regional Talent &amp; Coaching Unit – Email Banners</title>
<link rel="stylesheet" href="https://fonts.googleapis.com/css2?family=Montserrat:wght@700;800&family=Raleway:ital,wght@0,400;0,500;1,400&display=swap">
<style>
  :root {
    --canvas: #ffffff;
    --mint: #e1f6f0;
    --mint-soft: #f2fbf8;
    --ink: #111111;
    --ink-soft: #333333;
    --rule: #b9c4c2;
    --brand-red: #d62b21;
    --strip: #ffffff;
  }
  html, body {
    margin: 0;
    width: 1200px;
    height: 1200px;
    overflow: hidden;
    background: var(--canvas);
  }
  .canvas {
    position: relative;
    width: 1200px;
    height: 1200px;
  }
  .banner {
    position: absolute;
    left: 125px;
    width: 989px;
    height: 242px;
    background: linear-gradient(100deg, var(--mint-soft), var(--mint));
    overflow: hidden;
  }
  .banner--blue   { top: 63px; }
  .banner--red    { top: 330px; }
  .banner--purple { top: 597px; }
  .banner--teal   { top: 863px; }

  .banner__art {
    position: absolute;
    inset: 0;
    width: 100%;
    height: 100%;
  }
  .team-mark {
    position: absolute;
    left: 30px;
    top: 18px;
    width: 84px;
    height: 84px;
    border-radius: 50%;
    background: var(--brand-red);
  }
  .team-name {
    position: absolute;
    left: 124px;
    top: 52px;
    width: 340px;
  }
  .team-name__main {
    display: block;
    font-family: "Montserrat", sans-serif;
    font-weight: 800;
    font-size: 34px;
    letter-spacing: 0.5em;
    margin-right: -0.5em;
    line-height: 1;
    color: var(--ink);
    white-space: nowrap;
  }
  .team-name__sub {
    display: flex;
    align-items: center;
    justify-content: flex-end;
    gap: 10px;
    margin-top: 3px;
    font-family: "Raleway", sans-serif;
    font-weight: 500;
    font-size: 14.5px;
    color: var(--ink-soft);
    white-space: nowrap;
  }
  .team-name__sub::before {
    content: "";
    flex: 1;
    height: 1px;
    background: var(--rule);
  }
  .topic {
    position: absolute;
    left: 141px;
    top: 160px;
    font-family: "Raleway", sans-serif;
    font-weight: 500;
    font-size: 27px;
    letter-spacing: 0.01em;
    line-height: 1;
    color: var(--ink);
  }
  .partner {
    position: absolute;
    left: 0;
    bottom: 0;
    width: 439px;
    height: 31px;
    background: var(--strip);
    display: flex;
    align-items: center;
    justify-content: flex-end;
    gap: 7px;
    padding-right: 14px;
    box-sizing: border-box;
  }
  .partner__lead {
    font-family: "Raleway", sans-serif;
    font-style: italic;
    font-size: 9px;
    color: var(--ink-soft);
    margin-right: 6px;
  }
  .partner__mark {
    width: 20px;
    height: 20px;
    background: var(--brand-red);
  }
  .partner__name {
    font-family: "Montserrat", sans-serif;
    font-weight: 700;
    font-size: 18px;
    color: var(--ink-soft);
  }
</style>
</head>
<body>
<main class="canvas">

  <section class="banner banner--blue">
    <svg class="banner__art" viewBox="0 0 890 218" preserveAspectRatio="none">
      <defs>
        <linearGradient id="panel-blue" x1="0" y1="1" x2="1" y2="0">
          <stop offset="0" stop-color="#0f3a8e"/><stop offset="0.55" stop-color="#1c5fc4"/><stop offset="1" stop-color="#3aa0ee"/>
        </linearGradient>
        <pattern id="slot-blue" width="16" height="16" patternUnits="userSpaceOnUse">
          <rect width="16" height="16" fill="#ffffff"/><rect width="8" height="8" fill="#cccccc"/><rect x="8" y="8" width="8" height="8" fill="#cccccc"/>
        </pattern>
      </defs>
      <g role="img" aria-label="Soft blue bokeh background with glowing medical crosses">
        <polygon points="395,218 395,186 490,46 392,30 488,22 496,0 890,0 890,218" fill="url(#panel-blue)"/>
      </g>
      <polyline points="0,186 395,186 490,46 392,30 488,22 496,0" fill="none" stroke="#62e2c8" stroke-width="5"/>
      <ellipse cx="677" cy="113" rx="157" ry="80" fill="url(#slot-blue)" stroke="#5fd6d0" stroke-width="5"/>
    </svg>
    <div class="team-mark"></div>
    <div class="team-name"><span class="team-name__main">REGIONAL</span><span class="team-name__sub">TALENT &amp; COACHING UNIT</span></div>
    <div class="partner"><span class="partner__lead">...in collaboration with</span><span class="partner__mark"></span><span class="partner__name">Norvane</span></div>
  </section>

  <section class="banner banner--red">
    <svg class="banner__art" viewBox="0 0 890 218" preserveAspectRatio="none">
      <defs>
        <linearGradient id="panel-red" x1="0" y1="1" x2="1" y2="0">
          <stop offset="0" stop-color="#a8192a"/><stop offset="0.55" stop-color="#d63a4a"/><stop offset="1" stop-color="#f27a86"/>
        </linearGradient>
        <radialGradient id="photo-red" cx="0.5" cy="0.45" r="0.6">
          <stop offset="0" stop-color="#d8323c"/><stop offset="1" stop-color="#6a0c12"/>
        </radialGradient>
      </defs>
      <g role="img" aria-label="Soft red bokeh background with glowing medical crosses">
        <polygon points="395,218 395,186 490,46 392,30 488,22 496,0 890,0 890,218" fill="url(#panel-red)"/>
      </g>
      <polyline points="0,186 395,186 490,46 392,30 488,22 496,0" fill="none" stroke="#a91d2c" stroke-width="5"/>
      <g role="img" aria-label="Close-up image of red blood cells for the hematology topic">
        <ellipse cx="677" cy="113" rx="157" ry="80" fill="url(#photo-red)" stroke="#6b7fd8" stroke-width="5"/>
      </g>
    </svg>
    <div class="team-mark"></div>
    <div class="team-name"><span class="team-name__main">REGIONAL</span><span class="team-name__sub">TALENT &amp; COACHING UNIT</span></div>
    <div class="topic">TOPIC:HEMATOLOGY</div>
    <div class="partner"><span class="partner__lead">...in collaboration with</span><span class="partner__mark"></span><span class="partner__name">Norvane</span></div>
  </section>

  <section class="banner banner--purple">
    <svg class="banner__art" viewBox="0 0 890 218" preserveAspectRatio="none">
      <defs>
        <linearGradient id="panel-purple" x1="0" y1="1" x2="1" y2="0">
          <stop offset="0" stop-color="#3a1a4c"/><stop offset="0.55" stop-color="#6c3486"/><stop offset="1" stop-color="#b86ad8"/>
        </linearGradient>
        <pattern id="slot-purple" width="16" height="16" patternUnits="userSpaceOnUse">
          <rect width="16" height="16" fill="#ffffff"/><rect width="8" height="8" fill="#cccccc"/><rect x="8" y="8" width="8" height="8" fill="#cccccc"/>
        </pattern>
      </defs>
      <g role="img" aria-label="Soft purple bokeh background with glowing medical crosses">
        <polygon points="395,218 395,186 490,46 392,30 488,22 496,0 890,0 890,218" fill="url(#panel-purple)"/>
      </g>
      <polyline points="0,186 395,186 490,46 392,30 488,22 496,0" fill="none" stroke="#4b2456" stroke-width="5"/>
      <ellipse cx="677" cy="113" rx="157" ry="80" fill="url(#slot-purple)" stroke="#5d7fe0" stroke-width="5"/>
    </svg>
    <div class="team-mark"></div>
    <div class="team-name"><span class="team-name__main">REGIONAL</span><span class="team-name__sub">TALENT &amp; COACHING UNIT</span></div>
    <div class="partner"><span class="partner__lead">...in collaboration with</span><span class="partner__mark"></span><span class="partner__name">Norvane</span></div>
  </section>

  <section class="banner banner--teal">
    <svg class="banner__art" viewBox="0 0 890 218" preserveAspectRatio="none">
      <defs>
        <linearGradient id="panel-teal" x1="0" y1="1" x2="1" y2="0">
          <stop offset="0" stop-color="#2c6894"/><stop offset="0.55" stop-color="#4f9fc4"/><stop offset="1" stop-color="#9ae2ee"/>
        </linearGradient>
        <pattern id="slot-teal" width="16" height="16" patternUnits="userSpaceOnUse">
          <rect width="16" height="16" fill="#ffffff"/><rect width="8" height="8" fill="#cccccc"/><rect x="8" y="8" width="8" height="8" fill="#cccccc"/>
        </pattern>
      </defs>
      <g role="img" aria-label="Soft teal bokeh background with glowing medical crosses">
        <polygon points="395,218 395,186 490,46 392,30 488,22 496,0 890,0 890,218" fill="url(#panel-teal)"/>
      </g>
      <polyline points="0,186 395,186 490,46 392,30 488,22 496,0" fill="none" stroke="#3a78a3" stroke-width="5"/>
      <ellipse cx="677" cy="113" rx="157" ry="80" fill="url(#slot-teal)" stroke="#4f86d8" stroke-width="5"/>
    </svg>
    <div class="team-mark"></div>
    <div class="team-name"><span class="team-name__main">REGIONAL</span><span class="team-name__sub">TALENT &amp; COACHING UNIT</span></div>
    <div class="partner"><span class="partner__lead">...in collaboration with</span><span class="partner__mark"></span><span class="partner__name">Norvane</span></div>
  </section>

</main>
</body>
</html>
```